Website for HVAC products

We would like a website created that is simple and crisp while still mobile friendly. We currently have less than 30 products and we like the layout of the following site:
( http://www.pelmontsteelcraft.com/ ).

The color scheme has to blend well with our attached logo.

The menu bar needs to consist of:
Home -
Products- A page with all products
Sub-Pages- Air Handler Stands
Aluminum Condenser Stands
Air Distribution Products
A/C Cages
Accessories
Resources- A page with all specification sheets, instructions,
forms, video's, etc that will be elsewhere but can be
found in one place
Log In- A password protected area that will have special pricing
FAQ- Frequently asked questions / Sales Terms
Contact Us- Map, pics, contact form

The actual product sales page can be similar to the example website above with the following exceptions-
- Main product image with different images available
- Description
- Availability (Not Needed)
- Options (I need to be able to modify)
- Qty
- Add to Cart
- Current "Request a Quote" to be replaced with "Log In for
Distributor Pricing" and redirect to that page
- Description
- Related Products (Not Needed)
- Specifications
- Specifications Metric (Not Needed)

I have no preference on format (I currently use Wordpress) as long as it is user friendly to update/change content, products, images, etc.

In Summary-
The example website is a style we like but it's just an example
Please use our logo and colors
Please use general pictures for the slider until we have some
Please use the lorem ipsum text where info is needed and not
available

Thank you for your interest and I look forward to the creativity

Target Market(s)

HVAC Distributors

Industry/Entity Type

Hvac

Coding

Coded - Design and coding required

Requirements
Must have
• Layout similar to example website
• Mobile Device Capable

```html
<!DOCTYPE html>
<html lang="en">
<head>
<meta charset="utf-8">
<title>Kelvaro – Climate Products Company</title>
<link href="https://fonts.googleapis.com/css2?family=Open+Sans:wght@400;600&family=Raleway:wght@500;600;700;800&display=swap" rel="stylesheet">
<style>
:root{
  --blue:#2b6cc4;
  --red:#d2151b;
  --ink:#222;
  --grey-nav:#f2f2f2;
  --footer:#1e1e1e;
  --white:#fff;
  --steel:#8e9296;
  --steel-dark:#6f7377;
  --steel-light:#c4c7ca;
}
*{box-sizing:border-box;margin:0;padding:0}
html,body{width:1106px;height:1200px;overflow:hidden;background:var(--white)}
body{font-family:"Open Sans",sans-serif;color:var(--ink);position:relative}
a{color:inherit}
svg{display:block}
.wrap{position:absolute;left:91px;width:924px}

/* top bar */
.topbar{position:absolute;top:0;left:0;width:1106px;height:34px;background:var(--blue);color:var(--white);font-size:11.5px}
.topbar .contact{position:absolute;left:88px;top:0;height:34px;display:flex;align-items:center;gap:7px}
.topbar .account{position:absolute;right:91px;top:0;height:34px;display:flex;align-items:center;gap:7px}
.topbar .item{display:flex;align-items:center;gap:6px}
.topbar .sep{opacity:.9;margin:0 2px}

/* header */
.brand{position:absolute;left:89px;top:58px;display:flex;align-items:center;gap:10px}
.brand-mark{width:34px;height:34px;border-radius:50%;background:var(--red)}
.brand-name{font-family:"Raleway",sans-serif;font-weight:800;font-size:44px;color:var(--blue);letter-spacing:1px;line-height:1}
.brand-tag{position:absolute;left:89px;top:104px;font-family:"Raleway",sans-serif;font-weight:800;font-size:11px;color:var(--blue);letter-spacing:2.4px}
.search{position:absolute;left:475px;top:70px;width:408px;height:39px;border:1px solid #cfcfcf;display:flex}
.search input{flex:1;border:0;padding-left:12px;font:12px "Open Sans",sans-serif;color:#777;background:transparent}
.search button{width:47px;height:39px;margin:-1px -1px 0 0;border:0;background:var(--red);display:flex;align-items:center;justify-content:center}
.cart{position:absolute;left:903px;top:70px;display:flex;gap:8px}
.cart-title{font-size:13px;color:#555}
.cart-meta{font-size:9.5px;color:#888}

/* nav */
.nav{position:absolute;top:152px;left:0;width:1106px;height:41px;background:var(--grey-nav);border-bottom:2px solid var(--red)}
.nav ul{position:absolute;left:91px;width:924px;height:39px;list-style:none;display:flex;align-items:center;justify-content:space-between}
.nav .home{width:54px;height:39px;background:var(--red);display:flex;align-items:center;justify-content:center}
.nav li a{font-family:"Raleway",sans-serif;font-weight:600;font-size:13.5px;text-decoration:none;color:#222}
.nav ul li:nth-child(2){margin-left:40px}

/* hero */
.hero{top:211px;height:369px;background:linear-gradient(90deg,#4e8a2c 0%,#5e8d3a 35%,#7a6652 55%,#9a9a96 75%,#c8c6bd 100%);overflow:hidden}
.hero-copy{position:absolute;left:57px;top:97px;color:var(--white);font-family:"Raleway",sans-serif}
.hero-copy .kicker{font-weight:600;font-size:26px;letter-spacing:.3px}
.hero-copy h1{font-weight:800;font-size:38px;line-height:1.1;letter-spacing:.3px}
.hero-copy .sub{font-weight:600;font-size:23px;margin-top:4px}
.btn-shop{display:inline-block;margin-top:18px;margin-left:4px;background:var(--red);color:var(--white);font-weight:700;font-size:14px;padding:15px 22px;border-radius:2px;text-decoration:none;box-shadow:0 2px 4px rgba(0,0,0,.3)}
.dots{position:absolute;left:421px;top:323px;display:flex;gap:5px}
.dots span{width:16px;height:16px;border-radius:50%;border:1.5px solid var(--white)}
.dots span.on{background:var(--red)}

/* categories */
.cats{top:599px;height:200px}
.cats .arrow{position:absolute;top:0;width:17px;height:148px;background:#d3d3d3;display:flex;align-items:center;justify-content:center}
.cats .arrow.prev{left:0}.cats .arrow.next{right:0}
.cat{position:absolute;top:0;width:167px;text-align:center}
.cat .thumb{height:148px;border:3px solid #e9e9e9;background:var(--white)}
.thumb.stand{background:radial-gradient(ellipse 42% 46% at 50% 50%,var(--steel) 0%,var(--steel-light) 55%,var(--white) 100%)}
.thumb.condenser{background:radial-gradient(ellipse 48% 40% at 52% 48%,#a9adb1 0%,#d3d5d7 60%,var(--white) 100%)}
.thumb.box{background:radial-gradient(ellipse 45% 42% at 50% 52%,var(--steel-dark) 0%,#b3b6b9 58%,var(--white) 100%)}
.thumb.cage{background:radial-gradient(ellipse 38% 46% at 50% 48%,#9a9da0 0%,#d7d9db 58%,var(--white) 100%)}
.thumb.trim{background:radial-gradient(ellipse 50% 30% at 52% 45%,#a4a7aa 0%,#d6d8da 60%,var(--white) 100%)}
.cat .label{margin-top:16px;font-family:"Raleway",sans-serif;font-weight:600;font-size:13.5px;line-height:19px;color:#333}

/* newsletter */
.newsletter{position:absolute;top:849px;left:0;width:1106px;height:79px;background:var(--red)}
.newsletter .title{position:absolute;left:150px;top:17px;color:var(--white);font-family:"Raleway",sans-serif}
.newsletter .title small{display:block;font-size:13.5px;font-weight:600}
.newsletter .title strong{display:block;font-size:20px;font-weight:700}
.newsletter .icon{position:absolute;left:88px;top:19px}
.newsletter input{position:absolute;left:321px;top:19px;width:573px;height:36px;border:0;padding-left:22px;font:11px "Open Sans",sans-serif;color:#777}
.newsletter button{position:absolute;left:911px;top:17px;width:107px;height:41px;background:transparent;border:2px solid var(--white);color:var(--white);font:700 13px "Raleway",sans-serif;letter-spacing:.5px}

/* footer */
.footer{position:absolute;top:928px;left:0;width:1106px;height:272px;background:var(--footer);color:var(--white)}
.f-col{position:absolute;top:33px}
.f-col h3{font-family:"Raleway",sans-serif;font-weight:700;font-size:14px;margin-bottom:15px}
.f-col ul{list-style:none;font-size:11.5px;line-height:20.5px}
.f-col ul.u a{text-decoration:underline}
.f-col ul.plain li{line-height:23px}
.f-divider{position:absolute;top:20px;width:1px;height:185px;background:#2b2b2b}
.f-brand{position:absolute;left:88px;top:36px;display:flex;align-items:center;gap:6px}
.f-brand .mark{width:16px;height:16px;border-radius:50%;background:var(--white)}
.f-brand .name{font-family:"Raleway",sans-serif;font-weight:800;font-size:24px;letter-spacing:1px}
.f-about{position:absolute;left:91px;top:83px;width:215px;font-size:11.5px;line-height:20.5px;color:#e6e6e6}
.pay{position:absolute;left:91px;top:165px;display:flex;gap:3px}
.pay span{width:31px;height:20px;background:var(--white);border-radius:1px}
.pay span.badge{width:60px;margin-left:8px;border:2px solid #dcdcdc}
.f-contact{font-size:11.5px}
.f-contact li{display:flex;gap:12px;align-items:flex-start;margin-bottom:18px;line-height:19px}
.f-contact li svg{margin-top:4px;flex:none}
.f-bottom{position:absolute;top:210px;left:91px;width:924px;border-top:1px solid #2c2c2c;height:62px;display:flex;align-items:center;justify-content:space-between;font-size:11.5px}
.social{display:flex;align-items:center;gap:8px}
.social span.s{width:26px;height:26px;border-radius:4px;background:var(--white)}
.social .lbl{margin-right:5px}
</style>
</head>
<body>

<div class="topbar">
  <div class="contact">
    <span class="item"><svg width="12" height="12" viewBox="0 0 24 24"><path fill="#fff" d="M6.6 10.8a15 15 0 0 0 6.6 6.6l2.2-2.2c.3-.3.7-.4 1-.2 1.1.4 2.3.6 3.6.6.6 0 1 .4 1 1V20c0 .6-.4 1-1 1A17 17 0 0 1 3 4c0-.6.4-1 1-1h3.5c.6 0 1 .4 1 1 0 1.3.2 2.5.6 3.6.1.3 0 .7-.2 1z"/></svg>555.014.2290</span>
    <span class="sep">|</span>
    <span class="item"><svg width="14" height="11" viewBox="0 0 24 18"><rect width="24" height="18" rx="2" fill="#fff"/><path d="M1 2l11 8 11-8" stroke="#2b6cc4" stroke-width="2" fill="none"/></svg><a href="#">hello@kelvaro-demo.com</a></span>
  </div>
  <div class="account">
    <span class="item"><svg width="13" height="12" viewBox="0 0 24 22"><rect x="1" y="4" width="17" height="17" rx="2" fill="none" stroke="#fff" stroke-width="2.5"/><path d="M6 11l4 4 12-13" stroke="#fff" stroke-width="3" fill="none"/></svg>Checkout</span><span class="sep">|</span>
    <span class="item"><svg width="14" height="12" viewBox="0 0 24 21"><path fill="#fff" d="M12 21 2 11A6 6 0 0 1 12 3a6 6 0 0 1 10 8z"/></svg>Wishlist</span><span class="sep">|</span>
    <span class="item"><svg width="12" height="12" viewBox="0 0 24 24"><circle cx="12" cy="7" r="6" fill="#fff"/><path fill="#fff" d="M1 24c0-7 5-10 11-10s11 3 11 10z"/></svg>My Account</span><span class="sep">|</span>
    <span class="item"><svg width="10" height="12" viewBox="0 0 20 24"><path d="M5 11V7a5 5 0 0 1 10 0v4" stroke="#fff" stroke-width="3" fill="none"/><rect y="10" width="20" height="14" rx="2" fill="#fff"/></svg>Login</span><span class="sep">|</span>
    <span class="item"><svg width="12" height="12" viewBox="0 0 24 24"><path fill="#fff" d="M3 17 16 4l4 4L7 21H3zM18 2l2-2 4 4-2 2z"/></svg>Register</span>
  </div>
</div>

<header>
  <div class="brand"><span class="brand-mark"></span><span class="brand-name">KELVARO</span></div>
  <div class="brand-tag">CLIMATE PRODUCTS COMPANY</div>
  <form class="search"><input type="text" placeholder="SEARCH" aria-label="Search"><button type="button" aria-label="Search"><svg width="18" height="18" viewBox="0 0 24 24"><circle cx="10" cy="10" r="7" stroke="#fff" stroke-width="3" fill="none"/><path d="M15 15l7 7" stroke="#fff" stroke-width="3.5" stroke-linecap="round"/></svg></button></form>
  <div class="cart">
    <svg width="30" height="30" viewBox="0 0 30 30"><path d="M1 3h5l4 16h15l3-11H8" stroke="#d2151b" stroke-width="2.5" fill="none"/><path d="M10 11h16M11 15h13" stroke="#d2151b" stroke-width="1.5"/><circle cx="12" cy="25" r="2.5" fill="#d2151b"/><circle cx="23" cy="25" r="2.5" fill="#d2151b"/></svg>
    <div><div class="cart-title">My Cart</div><div class="cart-meta">0 Item(s) | $ 0 ▾</div></div>
  </div>
</header>

<nav class="nav">
  <ul>
    <li class="home"><svg width="22" height="20" viewBox="0 0 24 22"><path fill="#fff" d="M12 1 0 12h3v10h7v-7h4v7h7V12h3z"/></svg></li>
    <li><a href="#">PRODUCTS</a></li>
    <li><a href="#">RESOURCES</a></li>
    <li><a href="#">VIDEOS</a></li>
    <li><a href="#">LOGIN</a></li>
    <li><a href="#">FAQ</a></li>
    <li><a href="#">CONTACT US</a></li>
  </ul>
</nav>

<section class="wrap hero" role="img" aria-label="Photo of outdoor air conditioning condenser units on mulch beside a lawn">
  <div class="hero-copy">
    <div class="kicker">FORWARD THINKING.</div>
    <h1>PROVEN SOLUTIONS</h1>
    <div class="sub">Heating/Air Products</div>
    <a class="btn-shop" href="#">SHOP NOW &gt;&gt;</a>
  </div>
  <div class="dots"><span class="on"></span><span></span><span></span><span></span></div>
</section>

<section class="wrap cats">
  <div class="arrow prev"><svg width="8" height="14" viewBox="0 0 8 14"><path d="M7 1 1 7l6 6" stroke="#fff" stroke-width="2" fill="none"/></svg></div>
  <div class="cat" style="left:27px"><div class="thumb stand" role="img" aria-label="Product photo of a steel air handler stand"></div><div class="label">AIR HANDLER<br>STANDS</div></div>
  <div class="cat" style="left:203px"><div class="thumb condenser" role="img" aria-label="Product photo of an aluminum condenser stand"></div><div class="label">ALUMINUM CONDENSER<br>STANDS</div></div>
  <div class="cat" style="left:379px"><div class="thumb box" role="img" aria-label="Product photo of a sheet metal air distribution box"></div><div class="label">AIR DISTRIBUTION<br>PRODUCTS</div></div>
  <div class="cat" style="left:555px"><div class="thumb cage" role="img" aria-label="Product drawing of a wire A/C security cage"></div><div class="label">A/C CAGES</div></div>
  <div class="cat" style="left:731px"><div class="thumb trim" role="img" aria-label="Product photo of a folded sheet metal accessory"></div><div class="label">ACCESSORIES</div></div>
  <div class="arrow next"><svg width="8" height="14" viewBox="0 0 8 14"><path d="M1 1l6 6-6 6" stroke="#fff" stroke-width="2" fill="none"/></svg></div>
</section>

<section class="newsletter">
  <svg class="icon" width="42" height="36" viewBox="0 0 42 36"><g transform="rotate(-15 21 18)"><rect x="3" y="6" width="36" height="24" rx="2" fill="#fff"/><path d="M4 8l17 12 17-12" stroke="#d2151b" stroke-width="2.5" fill="none"/></g></svg>
  <div class="title"><small>NEWSLETTER</small><strong>SUBSCRIPTION</strong></div>
  <input type="email" placeholder="ENTER EMAIL ADDRESS" aria-label="Email address">
  <button type="button">SUBSCRIBE</button>
</section>

<footer class="footer">
  <div class="f-brand"><span class="mark"></span><span class="name">KELVARO</span></div>
  <p class="f-about">At vero eos et accusamus et iusto odio dignissimos ducimus qui blanditiis pra esentium voluptatum delen</p>
  <div class="pay"><span></span><span></span><span></span><span class="badge"></span></div>

  <div class="f-divider" style="left:316px"></div>
  <div class="f-col" style="left:346px"><h3>QUICK LINKS</h3>
    <ul class="u"><li><a href="#">Contact</a></li><li><a href="#">FAQ</a></li><li><a href="#">Delivery</a></li><li><a href="#">Returns</a></li><li><a href="#">Track Orders</a></li><li><a href="#">Subscribe</a></li></ul></div>
  <div class="f-divider" style="left:475px"></div>
  <div class="f-col" style="left:518px"><h3>EXTRAS</h3>
    <ul><li>Specials</li><li>New products</li><li>Top sellers</li><li>Our stores</li><li>Contact us</li><li>About us</li></ul></div>
  <div class="f-divider" style="left:628px"></div>
  <div class="f-col" style="left:668px"><h3>MY ACCOUNT</h3>
    <ul class="plain"><li>Delivery Information</li><li>Privacy Policy</li><li>Returns Policy</li><li>Terms and Conditions</li><li>FAQs</li></ul></div>
  <div class="f-divider" style="left:818px"></div>
  <div class="f-col" style="left:866px"><h3>CONTACT US</h3>
    <ul class="f-contact">
      <li><svg width="8" height="11" viewBox="0 0 16 22"><path fill="#fff" d="M8 0a8 8 0 0 1 8 8c0 6-8 14-8 14S0 14 0 8a8 8 0 0 1 8-8z"/><circle cx="8" cy="8" r="3" fill="#1e1e1e"/></svg><span>218 Harborline Ave.<br>Brookfield, CA 95012</span></li>
      <li><svg width="10" height="10" viewBox="0 0 24 24"><path fill="#fff" d="M6.6 10.8a15 15 0 0 0 6.6 6.6l2.2-2.2c.3-.3.7-.4 1-.2 1.1.4 2.3.6 3.6.6.6 0 1 .4 1 1V20c0 .6-.4 1-1 1A17 17 0 0 1 3 4c0-.6.4-1 1-1h3.5c.6 0 1 .4 1 1 0 1.3.2 2.5.6 3.6.1.3 0 .7-.2 1z"/></svg><span>555.014.2290</span></li>
      <li><svg width="11" height="9" viewBox="0 0 24 18"><rect width="24" height="18" rx="2" fill="#fff"/><path d="M1 2l11 8 11-8" stroke="#1e1e1e" stroke-width="2" fill="none"/></svg><a href="#">hello@kelvaro-demo.com</a></li>
    </ul></div>

  <div class="f-bottom">
    <span>Copyrights © 2016, Kelvaro. All Rights Reserved</span>
    <div class="social"><span class="lbl">Follow us on :</span><span class="s"></span><span class="s"></span><span class="s"></span><span class="s"></span><span class="s"></span><span class="s"></span></div>
  </div>
</footer>

</body>
</html>
```